Thornwell Deli Needs a Web Page!

Thornwell Deli is a gourmet sandwich shop in Baltimore, MD USA.
We are due to open in about a month or so and we need a great web page that looks cool and is easy to use. Our Concept supports local farmers, ranchers, fishmongers & purveyors. All of our menu items are made from scratch using fresh local ingredients.

Target Market(s)

Urban people on the go & Anyone who is hungry and likes a great sandwich

Industry/Entity Type

Shop

Requirements
Must have
• We must have these 8 tabs:
Home
Menus
Gallery
About Us
Media & Events
Hours & Location
Order Online
Contact Us

Also we would like our Logo to be a focal point
Our Color scheme is Red, Black, Grey, White and a reddish-orange
however any and all colors are great and will be considered
We would love an area on the page for our own food photos to be added.
Nice to have
• Baltimore Skyline
Order Online Now Button
Free Wi-Fi Symbol
Dine-In, Take Out, Delivery,
Business Lunches, Tail Gate Platters, Catering
Should not have
• No Stock images of food or chefs.
(We want to put all of our own food photos up later.)
No Pink.

```html
<!DOCTYPE html>
<html lang="en">
<head>
<meta charset="utf-8">
<title>Thornwell Deli</title>
<link href="https://fonts.googleapis.com/css2?family=Arimo:ital,wght@0,400;0,700;1,400&family=Fondamento&family=Lora:ital@1&display=swap" rel="stylesheet">
<style>
:root{
  --bg:#560609;
  --bg-light:#6a0a0e;
  --red:#c4070c;
  --red-dark:#8e0306;
  --orange:#f45a0a;
  --orange-light:#ff8a2a;
  --white:#ffffff;
  --text:#333333;
  --black:#050505;
  --gold:#f5a21b;
  --line:#d9d9d9;
}
*{margin:0;padding:0;box-sizing:border-box}
html,body{width:1200px;height:1072px;overflow:hidden}
body{background:radial-gradient(ellipse at 50% 20%,var(--bg-light),var(--bg) 70%);font-family:Arimo,Arial,sans-serif;position:relative;color:var(--text)}
.abs{position:absolute}

/* header */
.brand{left:183px;top:40px;display:flex;align-items:center;gap:10px}
.brand-dot{width:46px;height:46px;border-radius:50%;background:var(--red)}
.brand-name{font-weight:700;font-size:32px;color:var(--white);letter-spacing:.5px;white-space:nowrap}
.hours-seal{left:704px;top:-18px;width:92px;height:84px}
.order-box{left:862px;top:0;width:158px;height:79px;background:linear-gradient(#3a2a12,#120c05 45%,#000)}
.order-link{left:12px;top:11px;font-size:11px;color:var(--gold);text-decoration:underline;white-space:nowrap}
.free-tag{left:106px;top:16px;width:34px;height:16px;background:#c8ab21;color:#222;font-size:7px;font-weight:700;text-align:center;line-height:16px;transform:rotate(-6deg);border-radius:2px}
.order-icons{left:10px;top:46px;display:flex;gap:12px}
.order-icons svg{width:26px;height:24px}
.phone{left:864px;top:83px;display:flex;align-items:center;gap:14px;color:var(--gold);font-size:17px;white-space:nowrap}

/* nav */
.ribbon{top:158px;width:80px;height:50px;background:var(--red-dark)}
.ribbon.left{left:94px;clip-path:polygon(0 0,100% 0,100% 100%,0 100%,20% 50%)}
.ribbon.right{left:1026px;clip-path:polygon(0 0,100% 0,80% 50%,100% 100%,0 100%)}
.nav{left:171px;top:139px;width:858px;height:50px;background:linear-gradient(var(--red),#a20307);display:flex}
.nav a{color:var(--white);font-weight:700;font-size:11px;text-decoration:none;height:50px;line-height:50px;border-right:1px solid #9a0306;white-space:nowrap;text-align:center;flex:none}
.nav a:last-child{border-right:none}

/* hero */
.hero{left:180px;top:189px;width:840px;height:330px;background:var(--white)}
.hero-photo{left:9px;top:9px;width:822px;height:313px;background:linear-gradient(90deg,#b67a45 0%,#7c9a3a 38%,#f3f4f5 52%,#f3f4f5 78%,#d7a36a 100%)}
.hero-line{left:374px;top:44px;font-family:Lora,Georgia,serif;font-style:italic;font-size:17px;line-height:25px;color:#111;white-space:nowrap}
.hero-line em{color:var(--red)}
.arrow{top:135px;width:18px;height:36px;background:#222}
.arrow.prev{left:0;border-radius:0 18px 18px 0}
.arrow.next{right:0;border-radius:18px 0 0 18px}
.arrow svg{position:absolute;top:11px;left:4px}

/* features */
.features{left:180px;top:525px;width:840px;height:244px;background:linear-gradient(#ececec,var(--white) 40%);display:flex;padding:6px 3px}
.feature{width:210px;border-right:1px solid var(--line);position:relative}
.feature:last-child{border-right:none}
.feature-icon{position:absolute;left:12px;top:8px;width:58px;height:52px;border-radius:8px}
.feature h2{position:absolute;left:96px;top:4px;font-family:Fondamento,serif;font-weight:400;color:var(--red);font-size:30px;line-height:27px;white-space:nowrap}
.feature p{position:absolute;left:11px;top:81px;width:184px;font-size:10.8px;line-height:15.4px;color:#333;hyphens:auto;-webkit-hyphens:auto}
.btn{display:inline-block;background:linear-gradient(var(--orange-light),var(--orange));color:var(--white);font-weight:700;font-size:11px;border-radius:4px;height:22px;line-height:20px;padding:0 12px;border:1px solid #d24300;white-space:nowrap}
.feature .btn{position:absolute;left:58px;top:206px}

/* lower */
.lower{left:180px;top:773px;width:840px;height:243px;background:linear-gradient(#2c2c2c,var(--black))}
.col{top:0;height:243px}
.col h3{font-size:17px;font-weight:700;color:var(--white);padding:12px 0 10px;border-bottom:1px solid #444;white-space:nowrap}
.col-icon{position:absolute;top:10px;width:38px;height:30px;border-radius:5px}
.col p{font-style:italic;font-size:11px;line-height:15.4px;color:#e6e6e6}
.form label{position:absolute;left:0;font-size:11px;color:var(--white);white-space:nowrap}
.form .field{position:absolute;left:74px;width:180px;background:linear-gradient(#fff,#e6e6e6);border:1px solid #999}
.more{color:var(--red)}

/* footer */
.footer{top:1035px;font-size:11px;color:var(--white);white-space:nowrap}
.footer-links a{color:var(--white);text-decoration:none}
.footer-links span{margin:0 5px}
</style>
</head>
<body>

<header>
  <div class="abs brand"><span class="brand-dot"></span><span class="brand-name">Thornwell Deli</span></div>

  <svg class="abs hours-seal" viewBox="0 0 92 84" aria-label="Open 10am-9pm, closed Mondays">
    <circle cx="46" cy="40" r="40" fill="#c4070c"/>
    <g transform="rotate(-28 46 48)" font-family="Arimo,Arial,sans-serif" fill="#fff" text-anchor="middle">
      <text x="46" y="50" font-size="13" font-weight="700">10am-9pm</text>
      <text x="50" y="64" font-size="10" font-style="italic">Closed Mondays</text>
    </g>
  </svg>

  <div class="abs order-box">
    <a class="abs order-link">Order Online Now</a>
    <div class="abs free-tag">FREE!</div>
    <div class="abs order-icons">
      <svg viewBox="0 0 26 24" aria-label="Free Wi-Fi"><g fill="none" stroke="#3aa0d8" stroke-width="2"><path d="M6 6a10 10 0 0 0 0 12"/><path d="M20 6a10 10 0 0 1 0 12"/><path d="M9 9a5 5 0 0 0 0 6"/><path d="M17 9a5 5 0 0 1 0 6"/></g><circle cx="13" cy="12" r="2" fill="#3aa0d8"/><rect x="12" y="14" width="2" height="9" fill="#3aa0d8"/></svg>
      <svg viewBox="0 0 26 24" aria-label="Dine-in"><path d="M2 14 14 4 24 12 12 22Z" fill="#c2185b"/></svg>
      <svg viewBox="0 0 26 24" aria-label="Take out"><rect x="3" y="8" width="20" height="12" fill="#8bc34a"/><rect x="8" y="3" width="10" height="6" fill="#cddc39"/></svg>
      <svg viewBox="0 0 26 24" aria-label="Delivery"><rect x="4" y="3" width="18" height="19" fill="#ddd"/><path d="M2 12h10v-4l6 6-6 6v-4H2z" fill="#5cb85c"/></svg>
    </div>
  </div>

  <div class="abs phone">
    <svg width="26" height="18" viewBox="0 0 26 18" aria-label="Phone"><path d="M1 6C5 0 21 0 25 6l-4 3-3-3V4H8v2L5 9Z" fill="#fff"/><rect x="5" y="9" width="16" height="8" rx="2" fill="#fff"/><circle cx="13" cy="13" r="2.5" fill="#560609"/></svg>
    <span>+456 555 0148</span>
  </div>
</header>

<div class="abs ribbon left"></div>
<div class="abs ribbon right"></div>
<nav class="abs nav">
  <a style="width:84px">HOME</a><a style="width:74px">MENUS</a><a style="width:88px">GALLERY</a><a style="width:92px">ABOUT US</a><a style="width:129px">MEDIA &amp; EVENTS</a><a style="width:146px">HOURS &amp; LOCATION</a><a style="width:120px">ORDER ONLINE</a><a style="width:125px">CONTACT US</a>
</nav>

<section class="abs hero">
  <div class="abs hero-photo" role="img" aria-label="Food photo slideshow: sandwiches and fries">
    <p class="abs hero-line">Share Your <em>Luxury taste</em> with a<br>Totally Unforgettable Sweet &amp;<br>Delicious <em>Gifts !!</em></p>
    <div class="abs arrow prev"><svg width="10" height="14" viewBox="0 0 10 14"><path d="M8 1 2 7l6 6" stroke="#f45a0a" stroke-width="3" fill="none"/></svg></div>
    <div class="abs arrow next"><svg width="10" height="14" viewBox="0 0 10 14"><path d="M2 1l6 6-6 6" stroke="#f45a0a" stroke-width="3" fill="none"/></svg></div>
  </div>
</section>

<section class="abs features">
  <article class="feature">
    <div class="feature-icon" role="img" aria-label="Sandwich icon" style="background:linear-gradient(#f3e2b8,#7cb342)"></div>
    <h2>About<br>Us</h2>
    <p>Lorem ipsum dolor sit amet, consectetur adipiscing elit. Morbi quis mi urna. Integer euismod urna vitae nunc aliquet consectetur. Aliquam erat volutpat. Curabitur varius consectetur purus.</p>
    <a class="btn">Read more &#10095;</a>
  </article>
  <article class="feature">
    <div class="feature-icon" role="img" aria-label="Milkshake icon" style="left:30px;width:30px;background:linear-gradient(#f7e9dc,#8d6e63)"></div>
    <h2>Special<br>Offer</h2>
    <p>Lorem ipsum dolor sit amet, consectetur adipiscing elit. Morbi quis mi urna. Integer euismod urna vitae nunc aliquet consectetur. Aliquam erat volutpat. Curabitur varius consectetur purus.</p>
    <a class="btn">Read more &#10095;</a>
  </article>
  <article class="feature">
    <div class="feature-icon" role="img" aria-label="Shopping bag icon" style="background:linear-gradient(#fff7c0,#f5c400)"></div>
    <h2>Order<br>Online</h2>
    <p>Lorem ipsum dolor sit amet, consectetur adipiscing elit. Morbi quis mi urna. Integer euismod urna vitae nunc aliquet consectetur. Aliquam erat volutpat. Curabitur varius consectetur purus.</p>
    <a class="btn" style="left:60px">Read more &#10095;</a>
  </article>
  <article class="feature">
    <svg class="feature-icon" viewBox="0 0 44 44" style="width:44px;height:44px" aria-label="Location pin"><rect x="1" y="1" width="42" height="42" rx="5" fill="#8bc34a"/><circle cx="20" cy="16" r="9" fill="#d50000"/><path d="M20 25v14" stroke="#555" stroke-width="2"/></svg>
    <h2 style="left:62px">Our<br>Location</h2>
    <p>Lorem ipsum dolor sit amet, consectetur adipiscing elit. Morbi quis mi urna. Integer euismod urna vitae nunc aliquet consectetur. Aliquam erat volutpat. Curabitur varius consectetur purus.</p>
    <a class="btn" style="left:58px">Read more &#10095;</a>
  </article>
</section>

<section class="abs lower">
  <div class="abs col" style="left:14px;width:254px">
    <h3>Contact Us</h3>
    <div class="col-icon" role="img" aria-label="Envelope icon" style="left:208px;background:linear-gradient(#fff,#e9c98a)"></div>
    <div class="form">
      <label style="top:65px">Your name:</label>
      <div class="field" style="top:58px;height:26px"></div>
      <label style="top:97px">Email:</label>
      <div class="field" style="top:90px;height:26px"></div>
      <label style="top:129px">Query:</label>
      <div class="field" style="top:122px;height:63px"></div>
      <a class="btn abs" style="left:198px;top:190px;padding:0 8px">Send &#10095;</a>
    </div>
  </div>
  <div class="abs col" style="left:291px;width:254px">
    <h3>Media &amp; Events</h3>
    <div class="col-icon" role="img" aria-label="Megaphone icon" style="left:208px;background:linear-gradient(#7fd3ea,#1d8fb0)"></div>
    <p style="margin-top:13px">&#8220; In sed nibh ac velit ultrices interdum. Sed convallis leo sit amet turpis elementum ut fringilla lacus molestie. Cras dictum mauris id elit fermentum vel aliquam leo tempor. Duis nisi velit, elementum eu dignissim quis, aliquet non sapien. Phasellus porttitor mauris enim, quis dictum quam. &#8221;</p>
    <p style="margin-top:15px">Quis dictum, quam</p>
  </div>
  <div class="abs col" style="left:572px;width:254px">
    <h3>Delivery</h3>
    <div class="col-icon" role="img" aria-label="Delivery truck icon" style="left:195px;background:linear-gradient(#fff,#bbb)"></div>
    <p style="margin-top:13px">In sed nibh ac velit ultrices interdum. Sed convallis leo sit amet turpis elementum ut fringilla lacus molestie.</p>
    <p style="margin-top:15px">Cras dictum mauris id elit fermentum vel aliquam leo tempor. Duis nisi velit, elementum eu dignissim quis, aliquet non sapien <span class="more">...more</span></p>
  </div>
</section>

<footer>
  <p class="abs footer" style="left:181px">&copy; 2012 Thornwell Deli. All Right Receives</p>
  <p class="abs footer footer-links" style="right:193px">
    <a>Home</a><span>|</span><a>Menus</a><span>|</span><a>Gallery</a><span>|</span><a>About Us</a><span>|</span><a>Media &amp; Events</a><span>|</span><a>Hours &amp; Location</a><span>|</span><a>Order Online</a><span>|</span><a>Contact Us</a>
  </p>
</footer>

</body>
</html>
```